Harvest Ledger Partners Web Page

A modern and attractive Home Web Page for my rebranded Company, Harvest Ledger Partners. My existing website from my old brand is www.plumcorbelgroup.NET. I would like an up to date, modern and eye catching Home Web Page. It should entice the viewer to go further and stay on the site.
I will have my professional webmaster utilize this cover page for my redesigned site.

Target Market(s)

Privately held construction equipment rental companies looking to sell or have their business valued

Number of Pages Required

1 page

Font styles to use
Serif
Sans Serif

Colors
2f74b3
fec41b
fefbf7
faa54b
f37122
33a6d7

Requirements
Must have
• Above the fold I want to engage the customer so he stays on the sight. A call to action: "Free confidential conversation to discuss your unique situation and exit strategy or valuation of your business." Something like that in there.

Above the fold have menu and key offerings. Next section to summarize my business (again see plumcorbelgroup.NET for more info) with links to more details back in the site.
"A leading boutique M&A and Valuation advisory firm with over 30 years rental industry specific experience>
Tabs: Seller Representation
Business Valuations
Dependable Advice
Industry Articles
Industry Transactions/News
FAQ
Bottom should have key contact info

Key contact info.
Nice to have
• Logos of associations I belong to (on existing site at plumcorbelgroup.NET) (OTV and PLM only)
"Call Gus today for a free, confidential conversation regarding your unique situation and possible exit strategies."
Should not have
• Too much "busyness"

```html
<!DOCTYPE html>
<html lang="en">
<head>
<meta charset="utf-8">
<title>Harvest Ledger Partners — Home</title>
<link href="https://fonts.googleapis.com/css2?family=Raleway:wght@400;500;600;700&family=Open+Sans:wght@400;600&display=swap" rel="stylesheet">
<style>
:root{
  --stage:#b7cbdb;
  --white:#ffffff;
  --blue:#2f74b3;
  --sky:#33a6d7;
  --ice:#d3e8f6;
  --ice-soft:#e6f2fb;
  --navy:#0e1b2a;
  --ink:#1d2430;
  --muted:#6b7480;
  --orange:#f37122;
  --amber:#faa54b;
  --line:#d7dde3;
}
*{box-sizing:border-box;margin:0;padding:0}
html,body{width:1200px;height:3576px;overflow:hidden}
body{background:var(--stage);font-family:"Open Sans",Arial,sans-serif;color:var(--ink);position:relative}
.page{position:absolute;left:220px;top:18px;width:768px;height:3540px;background:var(--white);overflow:hidden}
.abs{position:absolute}
.heading{font-family:"Raleway",Arial,sans-serif}
.photo{position:absolute}
/* nav */
.site-nav{left:0;top:0;width:768px;height:52px;display:flex;align-items:center;justify-content:space-between;padding:0 52px}
.brand{display:flex;align-items:center;gap:6px;font-family:"Raleway",sans-serif;font-weight:600;font-size:10px;color:var(--blue)}
.brand i{width:12px;height:12px;background:var(--blue);display:block}
.menu{display:flex;font-family:"Raleway",sans-serif;font-size:8px;color:var(--ink)}
.menu a{padding:18px 9px;color:inherit;text-decoration:none}
.menu a.active{background:var(--sky);color:var(--white)}
/* hero */
.hero{left:0;top:52px;width:768px;height:400px;background:var(--ice)}
.hero-title{left:460px;top:92px;width:290px;font-size:29px;line-height:1.15;font-weight:600;color:var(--navy)}
.hero-copy{left:460px;top:222px;width:250px;font-size:10px;line-height:1.5;color:var(--ink)}
.btn{display:inline-block;background:var(--navy);color:var(--white);font-size:8px;font-family:"Raleway",sans-serif;padding:5px 16px;text-decoration:none}
.slider{left:650px;top:424px;display:flex;align-items:center;gap:10px;font-size:12px;color:var(--ink)}
/* intro */
.firm-mark{left:52px;top:478px;width:80px;height:80px;background:var(--ice);display:flex;align-items:center;justify-content:center}
.firm-mark i{width:26px;height:26px;background:var(--blue);display:block}
.firm-name{left:150px;top:500px;font-size:20px;color:var(--ink)}
.firm-sub{left:150px;top:530px;font-size:10px;color:var(--muted)}
.lead-title{left:52px;top:700px;width:310px;font-size:23px;line-height:1.25;color:var(--ink)}
.offerings{left:52px;top:768px;list-style:none;font-size:12px;line-height:1.6}
.orange-block{left:372px;top:668px;width:370px;height:212px;background:var(--orange)}
/* promise */
.promise{left:0;top:980px;width:768px;height:200px;background:var(--ice)}
.promise-panel{left:20px;top:988px;width:690px;height:184px;background:var(--ice-soft);box-shadow:0 6px 14px rgba(20,40,70,.12)}
.promise-bar{left:52px;top:1030px;width:5px;height:92px;background:var(--blue)}
.promise-text{left:78px;top:1030px;width:600px;font-size:33px;line-height:1.3;color:var(--blue);font-weight:500}
.value-box{left:420px;top:1440px;width:290px;height:182px;background:var(--ice);padding:40px 24px;font-size:20px;line-height:1.3;color:var(--navy);font-weight:500}
.about{left:52px;top:1660px;width:450px;font-size:10.5px;line-height:1.6}
.about p+p{margin-top:12px}
/* call band */
.call-band{left:0;top:1880px;width:768px;height:240px;background:var(--navy);color:var(--white);text-align:center;font-size:12px}
.call-band .lead{margin-top:50px}
.call-band .sub{margin-top:30px;line-height:1.6}
.call-band .phone{display:inline-flex;align-items:center;gap:8px;margin-top:4px}
.badges{left:0;top:2150px;width:768px;display:flex;justify-content:center;gap:110px}
.badge{width:130px;height:80px;background:#e9ecef;border-radius:6px}
/* news */
.section-title{font-size:22px;color:var(--ink);padding-left:14px;border-left:4px solid var(--blue)}
.news-title{left:52px;top:2350px}
.card{position:absolute;top:2420px;width:208px}
.card .photo{position:relative;height:160px}
.card h4{font-family:"Raleway",sans-serif;font-size:11px;font-weight:600;margin-top:18px}
.card p{font-size:8.5px;line-height:1.6;color:var(--muted);margin-top:8px}
.card a{display:block;font-size:8.5px;color:var(--muted);margin-top:12px;text-decoration:none}
/* faq */
.faq-title{left:52px;top:2800px}
.faq{left:0;top:2860px;width:768px;height:500px;background:var(--ice-soft)}
.faq-item{position:absolute;left:52px;width:664px;border-bottom:1px solid var(--line);font-size:9px;line-height:1.6}
.faq-item h5{font-size:9.5px;font-weight:600;padding-right:40px}
.faq-item p{margin-top:8px;color:var(--ink);padding-right:60px}
.faq-item svg{position:absolute;right:0;top:0}
/* footer */
.footer{left:0;top:3360px;width:768px;height:180px;background:var(--navy);color:#cfd6de;font-size:8.5px;line-height:1.9}
.footer .col{position:absolute;top:32px}
.footer h6{font-size:9px;color:var(--white);font-weight:600}
.social{display:flex;gap:6px;margin-top:4px}
.social i{width:12px;height:12px;background:#cfd6de;display:block}
.contact-row{display:flex;gap:6px;align-items:flex-start}
</style>
</head>
<body>
<div class="page">

  <header class="site-nav abs">
    <div class="brand"><i></i>Harvest Ledger Partners</div>
    <nav class="menu">
      <a class="active">Home</a><a>Seller Representation</a><a>Valuations</a><a>Articles</a><a>News</a><a>FAQ</a><a>Contact</a>
    </nav>
  </header>

  <section class="hero abs"></section>
  <div class="photo" role="img" aria-label="Yard of parked boom lifts and scissor lifts at a rental depot" style="left:52px;top:52px;width:388px;height:388px;background:linear-gradient(160deg,#d9dfe4 0%,#a9b2ba 45%,#6f7a70 70%,#3d4248 100%)"></div>
  <h1 class="hero-title heading abs">Lorem ipsum dolor sit amet, consetetur sadipscing.</h1>
  <div class="hero-copy abs">
    <p>Free confidential conversation to discuss your unique situation and exit strategy or valuation of your business.</p>
    <p style="margin-top:30px"><a class="btn">Learn More</a></p>
  </div>
  <div class="slider abs">
    <svg width="14" height="10" viewBox="0 0 14 10"><path d="M13 5H1M5 1L1 5l4 4" stroke="#1d2430" fill="none" stroke-width="1.2"/></svg>
    <span>1/4</span>
    <svg width="14" height="10" viewBox="0 0 14 10"><path d="M1 5h12M9 1l4 4-4 4" stroke="#1d2430" fill="none" stroke-width="1.2"/></svg>
  </div>

  <div class="firm-mark abs"><i></i></div>
  <div class="firm-name heading abs">Harvest Ledger Partners LLC</div>
  <div class="firm-sub abs">Gus Hollander, Principal</div>

  <h2 class="lead-title heading abs">The Leading M&amp;A Firm in the Rental Industry Today</h2>
  <ul class="offerings abs">
    <li>Business Sale Representation</li>
    <li>Equipment Rental</li>
    <li>Special Event Rentals</li>
    <li>Business Valuations</li>
    <li style="margin-top:14px"><a class="btn">Read More</a></li>
  </ul>
  <div class="orange-block abs"></div>
  <div class="photo" role="img" aria-label="Aerial view of a rental yard filled with colourful lifts" style="left:382px;top:690px;width:352px;height:200px;background:linear-gradient(135deg,#8a8f96 0%,#c9a24a 35%,#5d7fa3 60%,#9aa2aa 100%)"></div>

  <section class="promise abs"></section>
  <div class="promise-panel abs"></div>
  <div class="promise-bar abs"></div>
  <p class="promise-text heading abs">Our Promise to our Clients: Trust, Integrity, Experience, Results</p>

  <div class="photo" role="img" aria-label="Row of boom lift arms raised against a cloudy blue sky" style="left:52px;top:1288px;width:716px;height:252px;background:linear-gradient(180deg,#7fb2de 0%,#cfe0ef 45%,#4f7fae 70%,#c6562d 100%)"></div>
  <div class="value-box heading abs">Maximize the Value of Your Rental Company with Harvest Ledger Partners, LLC</div>

  <div class="about abs">
    <p>With our sole focus on the Rental Industry, we will maximize the value of your rental company and provide you with sound, reliable advice. We've sold hundreds of rental locations in our years.</p>
    <p>At Harvest Ledger Partners LLC we offer M&amp;A and Valuation Services specifically for equipment and special event rental business owners.</p>
  </div>

  <section class="call-band abs">
    <p class="lead">Call Gus today for a free, confidential conversation regarding your unique situation and possible exit strategies.</p>
    <p class="sub">For a confidential consultation,<br>call Gus Hollander</p>
    <p class="phone">
      <svg width="12" height="12" viewBox="0 0 24 24"><path fill="#fff" d="M6.6 10.8a15 15 0 006.6 6.6l2.2-2.2a1 1 0 011-.25 11.4 11.4 0 003.6.57 1 1 0 011 1V20a1 1 0 01-1 1A17 17 0 013 4a1 1 0 011-1h3.5a1 1 0 011 1c0 1.25.2 2.45.57 3.57a1 1 0 01-.25 1z"/></svg>
      (330) 555-0182
    </p>
  </section>

  <div class="badges abs">
    <div class="badge" role="img" aria-label="Association membership badge"></div>
    <div class="badge" role="img" aria-label="Association membership badge"></div>
  </div>

  <h3 class="section-title news-title heading abs">Industry News</h3>
  <article class="card" style="left:52px">
    <div class="photo" role="img" aria-label="Rental yard with lifts" style="background:linear-gradient(160deg,#9fc3e3,#b6a968 60%,#6c7078)"></div>
    <h4>Lorem ipsum dolor sit</h4>
    <p>Lorem ipsum dolor sit amet, consectetur adipiscing elit, sed do eiusmod tempor incididunt ut labore.</p>
    <a>Read More</a>
  </article>
  <article class="card" style="left:280px">
    <div class="photo" role="img" aria-label="Aerial view of rental equipment" style="background:linear-gradient(160deg,#8c9199,#c8a04c 45%,#5b7ea2)"></div>
    <h4>Lorem ipsum dolor sit</h4>
    <p>Lorem ipsum dolor sit amet, consectetur adipiscing elit, sed do eiusmod tempor incididunt ut labore.</p>
    <a>Read More</a>
  </article>
  <article class="card" style="left:508px">
    <div class="photo" role="img" aria-label="Boom lifts against the sky" style="background:linear-gradient(180deg,#86b6de,#d3e2ef 50%,#c4572e)"></div>
    <h4>Lorem ipsum dolor sit</h4>
    <p>Lorem ipsum dolor sit amet, consectetur adipiscing elit, sed do eiusmod tempor incididunt ut labore.</p>
    <a>Read More</a>
  </article>

  <h3 class="section-title faq-title heading abs">FAQ</h3>
  <section class="faq abs">
    <div class="faq-item" style="top:60px;height:196px">
      <h5>Lorem ipsum dolor sit amet, consetetur sadipscing elitr, sed diam?</h5>
      <svg width="16" height="16" viewBox="0 0 16 16"><circle cx="8" cy="8" r="7" fill="none" stroke="#1d2430"/><path d="M5 8h6" stroke="#1d2430"/></svg>
      <p>Lorem ipsum dolor sit amet, consetetur sadipscing elitr, sed diam nonumy eirmod tempor invidunt ut labore et dolore magna aliquyam erat, sed diam voluptua. At vero eos et accusam et justo duo dolores et ea rebum.</p>
      <p>Stet clita kasd gubergren, no sea takimata sanctus est lorem ipsum dolor sit amet. Lorem ipsum dolor sit amet, consetetur sadipscing elitr, sed diam nonumy eirmod tempor invidunt ut labore et dolore magna.</p>
      <p>At vero eos et accusam et justo duo dolores et ea rebum, stet clita kasd gubergren, no sea takimata sanctus est.</p>
    </div>
    <div class="faq-item" style="top:276px;height:80px">
      <h5>Lorem ipsum dolor sit amet, consetetur sadipscing elitr?</h5>
      <svg width="16" height="16" viewBox="0 0 16 16"><circle cx="8" cy="8" r="7" fill="none" stroke="#1d2430"/><path d="M5 8h6M8 5v6" stroke="#1d2430"/></svg>
      <p>Lorem ipsum dolor sit amet, consetetur sadipscing elitr, sed diam nonumy eirmod tempor invidunt ut labore et dolore.</p>
    </div>
    <div class="faq-item" style="top:376px;height:80px">
      <h5>Lorem ipsum dolor sit amet, consetetur sadipscing elitr?</h5>
      <svg width="16" height="16" viewBox="0 0 16 16"><circle cx="8" cy="8" r="7" fill="none" stroke="#1d2430"/><path d="M5 8h6M8 5v6" stroke="#1d2430"/></svg>
      <p>Lorem ipsum dolor sit amet, consetetur sadipscing elitr, sed diam nonumy eirmod tempor invidunt ut labore et dolore.</p>
    </div>
  </section>

  <footer class="footer abs">
    <div class="col" style="left:52px">
      <p>Home</p><p>About Us</p><p>Seller Representation</p><p>Business Valuations</p><p>Contact</p>
    </div>
    <div class="col" style="left:230px">
      <p>FAQ</p><p>Articles</p><p>News</p><p>Dependable Advice</p>
    </div>
    <div class="col" style="left:390px">
      <h6>Contact Us</h6>
      <div class="contact-row"><svg width="9" height="12" viewBox="0 0 12 16"><path fill="#cfd6de" d="M6 0a6 6 0 00-6 6c0 4.5 6 10 6 10s6-5.5 6-10a6 6 0 00-6-6zm0 8.5A2.5 2.5 0 116 3.5a2.5 2.5 0 010 5z"/></svg><span>118 Larkspur Road,<br>Brookfield, OH 44403</span></div>
      <div class="contact-row"><svg width="10" height="10" viewBox="0 0 24 24"><path fill="#cfd6de" d="M6.6 10.8a15 15 0 006.6 6.6l2.2-2.2a1 1 0 011-.25 11.4 11.4 0 003.6.57 1 1 0 011 1V20a1 1 0 01-1 1A17 17 0 013 4a1 1 0 011-1h3.5a1 1 0 011 1c0 1.25.2 2.45.57 3.57a1 1 0 01-.25 1z"/></svg><span>(330) 555-0182</span></div>
      <div class="contact-row"><svg width="10" height="8" viewBox="0 0 16 12"><rect x=".5" y=".5" width="15" height="11" fill="none" stroke="#cfd6de"/><path d="M1 1l7 6 7-6" fill="none" stroke="#cfd6de"/></svg><span>info@plumcorbelgroup.NET</span></div>
    </div>
    <div class="col" style="left:600px">
      <h6>Follow us on</h6>
      <div class="social"><i></i><i></i><i></i></div>
      <p style="margin-top:40px">plumcorbelgroup.NET</p>
    </div>
  </footer>

</div>
</body>
</html>
```